Liam Kovac Fitness Business Card

I Need a really cool and creative yet modern and cutting edge. I run a personal training company, I have a logo already which ill submit images of. Id like the base colors to be black and white with a little red as a highlight color. Charcoal grey is fine also. My clientele is mostly comprised of young professionals who are in touch with modern culture art and are interested in "cool" so if there was one thing i want this business card to be it sexy and cool.

Target Market(s)

young professionals who are image conscious, care about their health, looking and feeling good. They know what is cool and expect the best.

Industry/Entity Type

Training

Requirements
Must have
• - must be a 2 sided card
- must include the following:

Liam Kovac CPT
646 392 7105
Liam@LiamKovacFitness.example
www.LiamKovacFitness.example
Nice to have
• id like to see some unconventional shape ideas as well as conventional ones

```html
<!DOCTYPE html>
<html lang="en">
<head>
<meta charset="utf-8">
<title>Liam Kovac Fitness — Business Card</title>
<link rel="stylesheet" href="https://fonts.googleapis.com/css2?family=Jost:wght@500;600&family=Questrial&display=swap">
<style>
  :root {
    --stage: #ececec;
    --card-black: #111213;
    --card-black-soft: #2a2b2d;
    --card-white: #ffffff;
    --charcoal: #444648;
    --ink: #3a3b3d;
    --red: #e41c24;
    --red-soft: #ea5a62;
    --text-light: #ffffff;
  }
  * { box-sizing: border-box; margin: 0; padding: 0; }
  html, body { width: 1200px; height: 905px; overflow: hidden; }
  body {
    background: radial-gradient(ellipse at center, #fafafa 0%, var(--stage) 75%);
    display: flex;
    flex-direction: column;
    align-items: center;
    justify-content: center;
    gap: 44px;
  }
  .card {
    position: relative;
    width: 660px;
    height: 377px;
    border-radius: 34px;
    overflow: hidden;
    box-shadow: 0 10px 26px rgba(0,0,0,0.22);
  }

  .wordmark {
    font-family: "Questrial", sans-serif;
    font-size: 34px;
    letter-spacing: 0.5px;
    line-height: 1;
    white-space: nowrap;
  }

  /* Front side */
  .card--front {
    background: radial-gradient(ellipse at 45% 40%, var(--card-black-soft) 0%, var(--card-black) 70%);
    display: flex;
    align-items: center;
    justify-content: center;
  }
  .card--front .wordmark { color: var(--text-light); }

  /* Back side */
  .card--back { background: var(--card-white); }
  .card--back .wordmark {
    position: absolute;
    top: 82px;
    left: 50%;
    transform: translateX(-50%);
    color: var(--ink);
  }

  .name-band {
    position: absolute;
    left: 0;
    top: 188px;
    width: 300px;
    height: 88px;
    background: linear-gradient(90deg, var(--red) 0%, var(--red-soft) 100%);
    display: flex;
    flex-direction: column;
    justify-content: center;
    align-items: center;
    font-family: "Jost", sans-serif;
    font-weight: 600;
    font-size: 21px;
    line-height: 1.15;
    color: var(--text-light);
  }
  .contact-band {
    position: absolute;
    left: 300px;
    right: 0;
    top: 228px;
    height: 96px;
    background: linear-gradient(90deg, var(--charcoal) 0%, #2b2c2e 60%, var(--card-black) 100%);
    display: flex;
    flex-direction: column;
    justify-content: center;
    padding-left: 22px;
    font-family: "Jost", sans-serif;
    font-weight: 500;
    font-size: 15.5px;
    line-height: 1.35;
    color: var(--text-light);
    letter-spacing: 0.3px;
  }
</style>
</head>
<body>
  <section class="card card--front" aria-label="Card front">
    <span class="wordmark">Liam Kovac Fitness</span>
  </section>

  <section class="card card--back" aria-label="Card back">
    <span class="wordmark">Liam Kovac Fitness</span>
    <div class="name-band">
      <span class="name-band__name">Liam Kovac</span>
      <span class="name-band__title">CPT</span>
    </div>
    <div class="contact-band">
      <span class="contact-band__phone">T. 646 392 7105</span>
      <span class="contact-band__email">E: Liam@LiamKovacFitness.example</span>
      <span class="contact-band__web">www.LiamKovacFitness.example</span>
    </div>
  </section>
</body>
</html>
```